PDN Letterhead

We need a letterhead design that will be able to be used on all marketing products (letterhead, mail chimp, envelops, business cards, etc.) We are a law firm specializing primarily in transportation law but offer a wide range of services to our clients. We would like the design to be modern, simple, and professional. Our colors are black and gold, however, we've incorporated dark gray and white on other marketing products such as our website.

```html
<!DOCTYPE html>
<html lang="en">
<head>
<meta charset="utf-8">
<title>PDN Law Group Letterhead</title>
<link rel="stylesheet" href="https://fonts.googleapis.com/css2?family=Open+Sans:wght@400;600&family=Lato:wght@400&display=swap">
<style>
  :root {
    --backdrop: #e4e4e4;
    --paper: #ffffff;
    --paper-tint: #f7f7f7;
    --ink: #111111;
    --text: #4a4a4a;
    --gold: #b39468;
    --dark-bar: #1c1c1c;
  }
  html, body {
    margin: 0;
    padding: 0;
    width: 1040px;
    height: 1200px;
    overflow: hidden;
    background: var(--backdrop);
  }
  .letterhead {
    position: absolute;
    left: 80px;
    top: 33px;
    width: 880px;
    height: 1133px;
    background: var(--paper);
    box-shadow: 0 6px 24px rgba(0,0,0,0.18);
    font-family: "Open Sans", sans-serif;
    color: var(--text);
    overflow: hidden;
  }
  .letterhead__texture {
    position: absolute;
    inset: 18px 18px 14px 18px;
    background: linear-gradient(180deg, var(--paper-tint), #fbfbfb);
  }
  .brand {
    position: absolute;
    top: 98px;
    left: 0;
    right: 0;
    margin: 0;
    text-align: center;
    font-family: "Open Sans", sans-serif;
    font-weight: 400;
    font-size: 34px;
    line-height: 40px;
    color: var(--ink);
  }
  .letter {
    position: absolute;
    left: 82px;
    width: 712px;
    margin: 0;
    font-size: 14.5px;
    line-height: 17px;
  }
  .letter p { margin: 0; }
  .letter__date { top: 204px; }
  .letter__recipient { top: 238px; }
  .letter__salutation { top: 336px; }
  .letter__body {
    line-height: 25.6px;
    text-align: justify;
    hyphens: auto;
  }
  .letter__body--one { top: 383px; }
  .letter__body--two { top: 535px; }
  .letter__body--three { top: 636px; }
  .letter__closing { top: 767px; }
  .signature { top: 840px; }
  .signature__name {
    font-size: 17.5px;
    line-height: 22px;
    font-weight: 600;
    color: #3c3c3c;
  }
  .signature__title {
    margin-top: 5px !important;
    font-size: 14.5px;
  }
  .contact {
    position: absolute;
    left: 0;
    right: 0;
    top: 1063px;
    text-align: center;
    font-family: "Lato", sans-serif;
    font-size: 18px;
    line-height: 22px;
    color: var(--ink);
  }
  .contact__lines { display: inline-block; }
  .contact__primary {
    padding-bottom: 3px;
    border-bottom: 1px solid #8a8a8a;
  }
  .contact__secondary {
    margin-top: 3px;
    color: #222;
  }
  .contact__label, .contact__accent { color: var(--gold); }
  .footer-band {
    position: absolute;
    bottom: 0;
    left: 0;
    right: 0;
    height: 11px;
    display: flex;
  }
  .footer-band__gold { flex: 0 0 51.2%; background: var(--gold); }
  .footer-band__dark { flex: 1; background: var(--dark-bar); margin-left: 2px; }
</style>
</head>
<body>
  <main class="letterhead">
    <div class="letterhead__texture" role="img" aria-label="Faint repeating geometric background pattern in light grey"></div>

    <h1 class="brand">PDN Law Group</h1>

    <p class="letter letter__date">Issuing Date: May 5, 2018</p>

    <div class="letter letter__recipient">
      <p>Name Of Employee Mr. XYZABC</p>
      <p>Address of Employee</p>
      <p>Address Line 2 etc..</p>
    </div>

    <p class="letter letter__salutation">Dear Mr.XYZABC</p>

    <p class="letter letter__body letter__body--one">Lorem Ipsum has been the industry's standard dummy text ever since the 1500s, when an unknown printer took a galley of type and scrambled it to make a type specimen book. It has survived not only five centuries, but also the leap into electronic typesetting, remaining essentially unchanged. It was popularised in the 1960s with the release of transfer sheets containing Lorem Ipsum passages, and more recently with desktop publishing software and page layout tools including versions of Lorem Ipsum.</p>

    <p class="letter letter__body letter__body--two">Lorem Ipsum is simply dummy text of the printing and typesetting industry. Lorem Ipsum has been the industry's standard dummy text ever since the 1500s, when an unknown printer took a galley of type and scrambled it to make a type specimen book.</p>

    <p class="letter letter__body letter__body--three">It has survived not only five centuries, but also the leap into electronic typesetting, remaining essentially unchanged. It was popularised in the 1960s with the release of transfer sheets containing Lorem Ipsum passages.</p>

    <p class="letter letter__closing">Yours Sincerely</p>

    <div class="letter signature">
      <p class="signature__name">Daniel Harlow</p>
      <p class="signature__title">Managing Director</p>
    </div>

    <footer class="contact">
      <div class="contact__lines">
        <div class="contact__primary"><span class="contact__label">P:</span> 044-555 010 234 | <span class="contact__label">E:</span> info@pdnlaw.example | www.<span class="contact__accent">pdnlaw</span>.example</div>
        <div class="contact__secondary">18 Harbour Row, Suite 4, code 40210 Northland</div>
      </div>
    </footer>

    <div class="footer-band">
      <div class="footer-band__gold"></div>
      <div class="footer-band__dark"></div>
    </div>
  </main>
</body>
</html>
```